SKYBEND FITNESSRoll Out, A UNIQUE CONCIERGE MOBILE SERVICE LAUNCHING in SOUTH FLORIDA

I AM LOOKING TO ATTRACT LEADS FOR CONVERSION WHILE BRINGING OUR SERVICE TO LIFE IN THERE HANDS. WE SERVICE A VERY HIGHLY AFFLUENT CROWD. I would like those on a 5 x 7 two sided card

Target Market(s)

AFFLUENT

Industry/Entity Type

HEALTH AND FITNESS

Font styles to use
Other font styles liked:
• POPINS MED

Colors
0054AA
0677BA
7BADD7
CADEEF
E8F1F8
FFF300
FFF600
FEFA6F
FFFEC7
FFFEE8

Requirements
Must have
• space for postage I INCLUDED CONTENT
Nice to have
• CLASSY FUN LOOK
Should not have
• DULLNESs

```html
<!DOCTYPE html>
<html lang="en">
<head>
<meta charset="utf-8">
<title>SkyBend Fitness Postcard</title>
<link href="https://fonts.googleapis.com/css2?family=Fraunces:opsz,wght@9..144,700&family=Poppins:wght@400;500;700&family=Allura&display=swap" rel="stylesheet">
<style>
  :root{
    --bg:#ededed;
    --card-white:#ffffff;
    --panel-grey:#f0f0f0;
    --ink:#111111;
    --cyan:#6ccbdb;
    --sky:#7badd7;
    --deep-blue:#0677ba;
    --navy:#0054aa;
    --yellow:#fff300;
    --rule:#2a2a2a;
  }
  *{box-sizing:border-box;margin:0;padding:0}
  html,body{width:1200px;height:560px;overflow:hidden;background:var(--bg)}
  .canvas{position:relative;width:1200px;height:560px}

  /* Front */
  .card-front{position:absolute;left:106px;top:110px;width:487px;height:348px;overflow:hidden;background:var(--card-white)}
  .hero-photo{position:absolute;inset:0;
    background:linear-gradient(180deg,#6ccbdb 0%,#c9d3d8 28%,#8f9aa0 48%,#3e4a52 62%,#2b5f7f 80%,#13609a 100%)}
  .sky-splash{position:absolute;left:0;top:0}
  .headline-band{position:absolute;left:90px;top:58px;width:312px;height:62px;background:var(--card-white);border-radius:40px 8px 30px 10px}
  .front-headline{position:absolute;left:0;top:62px;width:487px;text-align:center;
    font-family:'Fraunces',Georgia,serif;font-weight:700;font-size:26px;line-height:27px;color:var(--ink)}
  .tagline{position:absolute;left:0;top:278px;width:487px;text-align:center;
    font-family:'Allura',cursive;font-size:46px;color:#ffffff}
  .corner{position:absolute;bottom:0}
  .corner-left{left:0}
  .corner-right{right:0}

  /* Back */
  .card-back{position:absolute;left:617px;top:110px;width:487px;height:348px;background:var(--card-white)}
  .message-panel{position:absolute;left:0;top:0;width:251px;height:348px;background:var(--panel-grey)}
  .brand-name{position:absolute;left:36px;top:46px;font-family:'Poppins',sans-serif;font-weight:500;font-size:27px;letter-spacing:1px;color:var(--cyan)}
  .brand-sub{position:absolute;left:76px;top:82px;font-family:'Poppins',sans-serif;font-weight:500;font-size:7px;letter-spacing:7px;color:var(--yellow)}
  .back-headline{position:absolute;left:36px;top:114px;width:200px;font-family:'Poppins',sans-serif;font-weight:700;font-size:16.5px;line-height:20px;color:var(--ink)}
  .service-line{position:absolute;left:38px;top:183px;width:200px;font-family:'Poppins',sans-serif;font-weight:400;font-size:9px;line-height:11.7px;color:var(--ink)}
  .offer-box{position:absolute;left:36px;top:233px;width:184px;height:43px;background:var(--card-white);border-radius:7px;padding:5px 8px;
    font-family:'Poppins',sans-serif;font-weight:400;font-size:8.6px;line-height:11.6px;color:var(--ink)}
  .offer-box strong{font-weight:700}
  .site-url{position:absolute;left:37px;top:284px;font-family:'Poppins',sans-serif;font-weight:700;font-size:15.5px;color:var(--ink)}
  .stamp-box{position:absolute;left:395px;top:35px;width:60px;height:70px;border:1px solid var(--rule)}
  .address-line{position:absolute;left:287px;width:168px;height:1px;background:var(--rule)}
</style>
</head>
<body>
<div class="canvas">

  <section class="card-front">
    <div class="hero-photo" role="img" aria-label="Photo of the branded mobile fitness truck parked on a rooftop with training straps and equipment laid out around it"></div>
    <svg class="sky-splash" width="487" height="120" viewBox="0 0 487 120" aria-hidden="true">
      <path d="M0 0H210C190 20 160 30 130 40C110 60 90 80 60 100L0 120Z" fill="var(--yellow)" opacity="0.9"/>
    </svg>
    <div class="headline-band"></div>
    <h1 class="front-headline">Get Fit on<br>Your Schedule</h1>
    <p class="tagline">Anywhere, Anytime</p>
    <svg class="corner corner-left" width="90" height="75" viewBox="0 0 90 75" aria-hidden="true">
      <path d="M33 0H74V41H66V8H33Z" fill="var(--cyan)"/>
      <path d="M16 17H57V57H49V25H16Z" fill="var(--yellow)"/>
      <path d="M0 34H42V75H34V42H0Z" fill="#ffffff"/>
    </svg>
    <svg class="corner corner-right" width="90" height="75" viewBox="0 0 90 75" aria-hidden="true">
      <path d="M57 0H90V41H82V8H57Z" fill="var(--cyan)"/>
      <path d="M16 17H57V57H49V25H16Z" fill="var(--yellow)" transform="translate(17 0)"/>
      <path d="M0 34H42V75H34V42H0Z" fill="#ffffff" transform="translate(0 0)"/>
    </svg>
  </section>

  <section class="card-back">
    <div class="message-panel"></div>
    <div class="brand-name">SKYBEND</div>
    <div class="brand-sub">FITNESS</div>
    <h2 class="back-headline">Transform Your Body and Your Game with SkyBend Fitness</h2>
    <p class="service-line">The Ultimate Mobile Concierge Fitness Service for Health, Golf, Tennis, Flexibility, Strength, and Agility</p>
    <div class="offer-box">Get Started with SkyBend Fitness Today <strong>FOR FREE CONSULTAION AND ASSESMENT GO TO</strong></div>
    <div class="site-url">www.skybendfitness.com</div>
    <div class="stamp-box"></div>
    <div class="address-line" style="top:168px"></div>
    <div class="address-line" style="top:199px"></div>
    <div class="address-line" style="top:231px"></div>
  </section>

</div>
</body>
</html>
```